Need this package pricing table turned into a professional looking and printable document

Please include the logo at the top. I would like this to be eye catching :)

Harbor Summit Program Packages:

Basic Harbor Summit Plan (System 1)
(Chatterbox ads + PPC + CRM)
Build out marketing campaigns in Bidmarks and Chatterbox ads
CRM build-out with automated lead follow up for two (2) weeks
Landing page build
A/B Split Testing on all campaigns
Call tracking
Campain tracking and monthly report

First Month: $2200 + ad spend ($1,500 minimum)
Ongoing: $1200/mo + ad spend ($1,500 minimum)
Length: 3 months, then month to month

Advanced Harbor Summit Plan (System 2)

System 1 & New Website (up to 5 pages) OR optimize current website + hyper optimized website hosting + On-page SEO + Reputation/Review Management + FSP
Landing page build
New website that is SEO optimized (up to 5 pages) OR optimizes your current website.
Off-site SEO (done every month)
Lightning fast website hosting
FSP (Findora Shop Page) set up and weekly updates
Email Marketing
Review generation system and management
Tracking and monthly report (Campain + Website)
Call Tracking

First Month: $3800 + ad spend ($1,500 minimum)
Ongoing: $2400/mo + ad spend ($1,500 minimum)
Length: 6 months, then month to month

Premier Harbor Summit Plan (System 3)
System 1 & 2 + New Website (up to 10 pages) OR optimize current website + monthly off-page SEO + Monthly press release + social media management + Email Marketing
Landing page build
New website that is SEO optimized (up to 10 pages) OR optimizes your current website
Quality backlink building
Monthly Press Release
Cocial media management
Tracking and monthly report (Campain + Website + Emails)
Call Tracking
First Month: $6000+ ad spend ($1,500 minimum)
Ongoing: $3700/mo + ad spend ($1,500 minimum)

CB/Bidmarks extra niche/location - $600/mo
SEO Extra Niche - $600/mo
Multi location Microsites - $1,100 build then $600/mo SEO

```html
<!DOCTYPE html>
<html lang="en">
<head>
<meta charset="utf-8">
<title>Harbor Summit Program Packages</title>
<link href="https://fonts.googleapis.com/css2?family=Oswald:wght@500&family=Roboto+Condensed:wght@400&family=Roboto:wght@700&display=swap" rel="stylesheet">
<style>
  :root {
    --page-bg: #e7e8ea;
    --brand-blue: #2b8fd3;
    --tagline: #e9a81f;
    --banner-start: #8b1c6c;
    --banner-end: #cc1a62;
    --header-top: #b8176a;
    --header-bottom: #7d1d6e;
    --panel-teal: #2a9c98;
    --text-light: #ffffff;
    --price-accent: #f4ea43;
  }
  * { box-sizing: border-box; margin: 0; padding: 0; }
  html, body { width: 1200px; height: 815px; overflow: hidden; }
  body {
    background: var(--page-bg);
    font-family: "Roboto Condensed", "Arial Narrow", sans-serif;
    position: relative;
  }
  .brand {
    position: absolute; top: 24px; left: 0; width: 1200px;
    display: flex; flex-direction: column; align-items: center;
  }
  .brand-mark { width: 66px; height: 66px; background: var(--brand-blue); }
  .brand-name {
    font-family: "Roboto", Arial, sans-serif; font-weight: 700;
    font-size: 21px; line-height: 1.1; color: var(--brand-blue); margin-top: 8px;
  }
  .brand-tagline {
    font-family: "Roboto", Arial, sans-serif; font-weight: 700;
    font-size: 12px; line-height: 1.1; color: var(--tagline); margin-top: 1px;
  }
  .banner {
    position: absolute; top: 143px; left: 165px; width: 869px; height: 51px;
    background: linear-gradient(90deg, var(--banner-start), var(--banner-end));
    display: flex; align-items: center; justify-content: center;
  }
  .banner h1 {
    font-family: "Oswald", "Arial Narrow", sans-serif; font-weight: 500;
    font-size: 26px; color: var(--text-light); letter-spacing: 1px;
  }
  .package {
    position: absolute; top: 211px; width: 263px; height: 583px;
    background: var(--panel-teal);
  }
  .package--basic { left: 165px; }
  .package--advanced { left: 468px; }
  .package--premier { left: 772px; }
  .package-header {
    height: 130px;
    background: linear-gradient(180deg, var(--header-top), var(--header-bottom));
    clip-path: polygon(0 0, 100% 0, 100% 78%, 50% 100%, 0 78%);
    color: var(--text-light);
    text-align: center;
    font-size: 17.5px; line-height: 1.35;
    padding-top: 26px;
  }
  .package-body {
    padding: 18px 8px 0 14px;
    color: var(--text-light);
    font-size: 9.6px; line-height: 1.45;
  }
  .features, .pricing, .addons { list-style: none; }
  .features li, .pricing li, .addons li { position: relative; padding-left: 10px; }
  .features li::before, .pricing li::before, .addons li::before {
    content: ""; position: absolute; left: 0; top: 6px;
    width: 3px; height: 3px; border-radius: 50%; background: var(--text-light);
  }
  .pricing, .addons { margin-top: 11px; }
  .accent { color: var(--price-accent); }
</style>
</head>
<body>
  <header class="brand">
    <span class="brand-mark"></span>
    <span class="brand-name">Harbor Summit Marketing</span>
    <p class="brand-tagline">More Calls. More Leads. Less Stress.</p>
  </header>

  <div class="banner"><h1>CHOOSE YOUR PACKAGE</h1></div>

  <section class="package package--basic">
    <div class="package-header">Basic Harbor Summit Plan<br>(System 1)</div>
    <div class="package-body">
      <ul class="features">
        <li>Basic Harbor Summit Plan (System 1)<br>(Chatterbox ads + PPC + CRM)<br>Build out marketing campaigns in Bidmarks and</li>
        <li>Chatterbox ads</li>
        <li>CRM build-out with automated lead follow up for</li>
        <li>two (2) weeks</li>
        <li>Landing page build</li>
        <li>A/B Split Testing on all campaigns</li>
        <li>Call tracking</li>
        <li>Campain tracking and monthly report</li>
      </ul>
      <ul class="pricing">
        <li>First Month: <span class="accent">$2200</span> + ad spend (<span class="accent">$1,500</span> minimum)</li>
        <li>Ongoing: <span class="accent">$1200</span>/mo + ad spend (<span class="accent">$1,500</span> minimum)</li>
        <li>Length: <span class="accent">3</span> months, then month to month</li>
      </ul>
    </div>
  </section>

  <section class="package package--advanced">
    <div class="package-header">Advanced Harbor Summit Plan<br>(System 2)</div>
    <div class="package-body">
      <ul class="features">
        <li>System 1 &amp; New Website (up to 5 pages) OR optimize<br>current website + hyper optimized website hosting<br>+ On-page SEO + Reputation/Review Management + FSP</li>
        <li>Build out marketing campaigns in Bidmarks and Chatterbox ads</li>
        <li>CRM build-out with automated lead follow up for two (2) weeks</li>
        <li>Landing page build</li>
        <li>A/B Split Testing on all campaigns</li>
        <li>New website that is SEO optimized (up to 5 pages)</li>
        <li>OR optimizes your current website.</li>
        <li>Off-site SEO (done every month)</li>
        <li>Lightning fast website hosting</li>
        <li>FSP (Findora Shop Page) set up and weekly updates</li>
        <li>Email Marketing</li>
        <li>Review generation system and management</li>
        <li>Tracking and monthly report (Campain + Website)</li>
        <li>Call Tracking</li>
      </ul>
      <ul class="pricing">
        <li>First Month: <span class="accent">$3800</span> + ad spend (<span class="accent">$1,500</span> minimum)</li>
        <li>Ongoing: <span class="accent">$2400</span>/mo + ad spend (<span class="accent">$1,500</span> minimum)</li>
        <li>Length: <span class="accent">6</span> months, then month to month</li>
      </ul>
    </div>
  </section>

  <section class="package package--premier">
    <div class="package-header">Premier Harbor Summit Plan<br>(System 3)</div>
    <div class="package-body">
      <ul class="features">
        <li>System 1 &amp; 2 + New Website (up to 10 pages) OR optimize<br>current website + monthly off-page SEO + Monthly press release<br>+ social media management + Email Marketing</li>
        <li>Build out marketing campaigns in Bidmarks and Chatterbox ads</li>
        <li>CRM build-out with automated lead follow up for two (2) weeks</li>
        <li>Landing page build</li>
        <li>A/B Split Testing on all campaigns</li>
        <li>New website that is SEO optimized (up to 10 pages)</li>
        <li>OR optimizes your current website</li>
        <li>Off-site SEO (done every month)</li>
        <li>Quality backlink building</li>
        <li>Monthly Press Release</li>
        <li>FSP (Findora Shop Page) set up and weekly updates</li>
        <li>Review generation system and management</li>
        <li>Cocial media management</li>
        <li>Tracking and monthly report (Campain + Website + Emails)</li>
        <li>Call Tracking</li>
        <li>First Month: <span class="accent">$6000</span>+ ad spend (<span class="accent">$1,500</span> minimum)</li>
        <li>Ongoing: <span class="accent">$3700</span>/mo + ad spend (<span class="accent">$1,500</span> minimum)</li>
        <li>Length: 6 months, then month to month</li>
      </ul>
      <ul class="addons">
        <li>CB/Bidmarks extra niche/location - <span class="accent">$600</span>/mo</li>
        <li>SEO Extra Niche - <span class="accent">$600</span>/mo</li>
        <li>Multi location Microsites - <span class="accent">$1,100</span> build then <span class="accent">$600</span>/mo SEO</li>
      </ul>
    </div>
  </section>
</body>
</html>
```